Independent International Travel Romantic Comedy Film Poster Design

We need a fun, eye-catching film poster for a romantic comedy shot in San Francisco and throughout the country of Turkey. Very open to cute ideas that grab attention as a small thumbnail.

If your design includes photos and is chosen we would like to take photos of our actors in similar position to replace for your final delivery.

Story: A girl books a trip with her boyfriend, but when he breaks up with her, she is stuck with One-Way Detour tickets in his name. Her friends convince her to find a guy with her ex-boyfriend's name to still go on the trip.

Our film trailer for ideas: https://www.reelhopper.net/watch?v=7Qp4LmN2zRx

Our temp website for ideas: http://www.OneWayDetourFilm.com

Target Market(s)

Young Travelers, Independent Film Lovers, Millennials, 90's RomCom Fans, The Marnie Colter Journals fans

Industry/Entity Type

Travel

Requirements
Must have
• We really want the poster thumbnail to stand out when seen with other independent films on Streamlark.com/ondemand
Nice to have
• Some of our ideas include a "pop-up book map" with characters and iconic landmarks. We like posters for movies like Velvet Errand (pink version), Quietly Tangled, Woman Near the Ferry, Watch Lark Hum, Twelve Rainy Tuesdays, Tide Nine...

```html
<!DOCTYPE html>
<html lang="en">
<head>
<meta charset="utf-8">
<title>One-Way Detour — Poster</title>
<link rel="stylesheet" href="https://fonts.googleapis.com/css2?family=Bebas+Neue&family=Raleway:wght@300&family=Yellowtail&display=swap">
<style>
  :root {
    --paper: #ffffff;
    --ink-blue: #4a70a2;
    --title-blue: #5a6f98;
    --band-khaki: #c0b47f;
    --band-cream: #fbf4c3;
    --script-yellow: #f7f0a0;
    --photo-dark: #3b3121;
    --photo-mid: #8a7040;
    --photo-gold: #f2c95e;
  }
  html, body {
    margin: 0;
    padding: 0;
    overflow: hidden;
    background: var(--paper);
  }
  .poster {
    position: relative;
    width: 927px;
    height: 1200px;
    overflow: hidden;
    background: var(--paper);
  }
  .artwork {
    position: absolute;
    inset: 0;
    width: 927px;
    height: 1200px;
  }
  .tagline {
    position: absolute;
    margin: 0;
    font-family: "Bebas Neue", "Oswald", sans-serif;
    font-weight: 400;
    color: var(--ink-blue);
    line-height: 1;
    white-space: nowrap;
  }
  .tagline--love {
    left: 162px;
    top: 36px;
    font-size: 126px;
  }
  .tagline--sometimes {
    left: 410px;
    top: 818px;
    font-size: 114px;
  }
  .film-title {
    position: absolute;
    left: 10px;
    top: 1030px;
    margin: 0;
    white-space: nowrap;
    line-height: 1;
    font-weight: 400;
  }
  .film-title__script {
    font-family: "Yellowtail", cursive;
    font-size: 82px;
    color: var(--script-yellow);
    margin-right: 6px;
  }
  .film-title__main {
    font-family: "Raleway", sans-serif;
    font-weight: 300;
    font-size: 94px;
    color: var(--title-blue);
    letter-spacing: 2px;
  }
</style>
</head>
<body>
<main class="poster">
  <svg class="artwork" viewBox="0 0 1159 1500" xmlns="http://www.w3.org/2000/svg">
    <defs>
      <radialGradient id="sunset-glow" cx="0.55" cy="0.5" r="0.6">
        <stop offset="0" stop-color="var(--photo-gold)"/>
        <stop offset="0.35" stop-color="var(--photo-mid)"/>
        <stop offset="1" stop-color="var(--photo-dark)"/>
      </radialGradient>
      <filter id="band-shadow" x="-5%" y="-20%" width="110%" height="140%">
        <feDropShadow dx="0" dy="-3" stdDeviation="5" flood-color="#000" flood-opacity="0.18"/>
      </filter>
    </defs>

    <path class="plane-photo" role="img"
          aria-label="Photo of a couple in silhouette about to kiss at sunset, wine glasses in the foreground, framed in an airplane shape"
          fill="url(#sunset-glow)"
          d="M950 60 Q1010 35 1065 110 Q1085 150 1015 205 L720 500 L1100 590 Q1170 610 1140 660 L990 960 Q965 1000 930 980 Q885 950 890 900 L900 790 L620 680 L480 1100 Q465 1150 420 1135 L370 1115 Q342 1100 342 1060 L340 510 Q335 490 310 480 L40 290 Q-10 255 5 215 Q20 180 70 190 L430 340 Z"/>

    <g class="torn-band" filter="url(#band-shadow)">
      <path fill="var(--band-cream)"
            d="M0 1172 L120 1168 L180 1160 L260 1175 L330 1165 L420 1178 L470 1150 L560 1172 L640 1148 L700 1170 L790 1160 L860 1176 L950 1162 L1040 1176 L1100 1165 L1159 1170 L1159 1500 L0 1500 Z"/>
      <path fill="var(--band-khaki)"
            d="M0 1205 L90 1200 L150 1192 L230 1208 L300 1196 L380 1212 L460 1188 L540 1206 L620 1186 L700 1204 L760 1215 L830 1196 L920 1210 L1000 1194 L1080 1208 L1159 1198 L1159 1500 L0 1500 Z"/>
    </g>
  </svg>

  <h2 class="tagline tagline--love">LOVE..</h2>
  <h2 class="tagline tagline--sometimes">IS SOMETIMES</h2>

  <h1 class="film-title">
    <span class="film-title__script">one-way</span><span class="film-title__main">DETOUR</span>
  </h1>
</main>
</body>
</html>
```